KELBROOK PAINTING

We are a painting company. We paint residential, commercial and strata jobs. I need the website to be very sharp, neat and elegant. I've attached our logo. the Logo needs to be embossed as a gold color and the background like a Matt black. I need these tabs:

• HOME • ABOUT US • SERVICES • TESTIMONIALS • SHOWCASE • CONTACT US

Be creative and innovative in your style.
take this as an example to just get the gist of what I'm expecting. If you can better it then the job is yours!

http://gilmarchcoatings.com.au/contact.html

I look forward to seeing your artwork :)

#These are the links to my logo in PSD format.

https://www.filevaultzy.com/s/qrtxwpl3k8hvb2z/Kelbrook%20Painting%20Luxury%20Gold.rar

https://www.filevaultzy.com/sh/hvbdkwpa2m7ycq5/XuoP7-bqLk

Painting

• Making the Logo embossed like the artworks i have attached is definitely a necessity.

Can you let me know if this is possible to apply to the website.

thank you

```html
<!DOCTYPE html>
<html lang="en">
<head>
<meta charset="utf-8">
<title>Kelbrook Painting — Our Services</title>
<link rel="stylesheet" href="https://fonts.googleapis.com/css2?family=Lato:wght@300;400;700&family=Montserrat:wght@600&family=Arimo:wght@700&display=swap">
<style>
  :root {
    --bg: #222222;
    --header-bg: #252525;
    --text: #ececec;
    --white: #ffffff;
    --gold: #d9a21c;
    --rule: #8a8a8a;
  }
  * { margin: 0; padding: 0; box-sizing: border-box; }
  html, body {
    width: 1200px; height: 1000px; overflow: hidden;
    background: var(--bg); color: var(--text);
    font-family: "Lato", sans-serif;
  }
  .site-header {
    position: relative; height: 70px; background: var(--header-bg);
  }
  .brand {
    position: absolute; left: 241px; top: 27px;
  }
  .brand-name {
    font-family: "Lato", sans-serif; font-weight: 700; font-size: 16px;
    color: var(--white); line-height: 18px; letter-spacing: 0.2px;
  }
  .main-nav {
    position: absolute; right: 211px; top: 0; height: 70px;
    display: flex;
  }
  .main-nav a {
    position: relative; display: block; padding: 0 12px; line-height: 80px;
    font-family: "Arimo", sans-serif; font-weight: 700; font-size: 10px;
    color: var(--white); text-decoration: none;
  }
  .main-nav a:last-child { padding-right: 0; }
  .main-nav a.is-active::before {
    content: ""; position: absolute; left: -5px; right: -5px; top: 0;
    height: 4px; background: var(--gold);
  }
  .spectrum-line {
    height: 4px;
    background: linear-gradient(90deg, #d4161c 0%, #b41fa0 18%, #3a2fc8 32%, #1f8fd8 45%, #20b8a0 55%, #2fc23a 68%, #d8d018 82%, #e0261a 100%);
  }
  .services {
    width: 750px; margin-left: 239px; padding-top: 35px;
  }
  .section-title {
    text-align: center; font-family: "Montserrat", sans-serif; font-weight: 600;
    font-size: 19px; letter-spacing: 1.5px; color: var(--white);
  }
  .service-images {
    display: flex; justify-content: space-between;
    padding: 0 35px 0 29px; margin-top: 52px;
  }
  .service-photo { width: 186px; height: 186px; border-radius: 50%; }
  .photo-swatches { background: linear-gradient(160deg, #7a2fa8 0%, #3d3fc0 40%, #2e7fd8 70%, #8fc8ee 100%); }
  .photo-painter { background: radial-gradient(circle at 55% 50%, #e6cc52 0%, #cfae36 60%, #a88c28 100%); }
  .photo-room { background: linear-gradient(180deg, #8ba159 0%, #7f9a4e 60%, #c8c8b8 100%); }
  .divider { border: 0; border-top: 1px solid var(--rule); margin-top: 42px; }
  .intro, .service p {
    font-weight: 300; font-size: 15px; line-height: 18.4px;
    text-align: justify; hyphens: auto; -webkit-hyphens: auto;
    letter-spacing: 0.6px;
  }
  .intro { margin-top: 18px; }
  .service h2 {
    font-weight: 700; font-size: 16px; color: var(--white);
    letter-spacing: 0.3px; margin: 35px 0 18px;
  }
  .service p + p.gap { margin-top: 18px; }
</style>
</head>
<body>
  <header class="site-header">
    <div class="brand">
      <span class="brand-name">KELBROOK PAINTING</span>
    </div>
    <nav class="main-nav">
      <a href="#">HOME</a>
      <a href="#">ABOUT US</a>
      <a href="#" class="is-active">SERVICES</a>
      <a href="#">TESTIMONIALS</a>
      <a href="#">SHOWCASE</a>
      <a href="#">CONTACT US</a>
    </nav>
  </header>
  <div class="spectrum-line"></div>

  <main class="services">
    <h1 class="section-title">OUR SERVICES</h1>
    <div class="service-images">
      <div class="service-photo photo-swatches" role="img" aria-label="Fanned paint colour swatch cards in purples and blues"></div>
      <div class="service-photo photo-painter" role="img" aria-label="Painter on a ladder painting a yellow wall"></div>
      <div class="service-photo photo-room" role="img" aria-label="Green painted living room with a white cabinet"></div>
    </div>
    <hr class="divider">
    <p class="intro">At vero eos et accusamus et iusto odio dignissimos ducimus qui blanditiis praesentium voluptatum deleniti atque corrupti quos dolores et quas molestias excepturi sint occaecati cupiditate non provident, similique sunt in culpa qui officia</p>

    <section class="service">
      <h2>COMMERCIAL PAINTING</h2>
      <p>We offer outstanding commercial building painting services at exceptional prices. We handle both large and small commercial painting projects. All projects work has been performed by experienced, fully-trained painters. We understand the commercial painting process thoroughly and know what it takes to complete a project properly, within budget and on time.</p>
      <p class="gap">Our range of interior and exterior commercial painting projects include warehouses, storage facilities, office buildings, entertainment venues, metal and steel –clad buildings, transportation facilities, underground parking garages, apartments and business office interiors, multi –unit residential buildings, high rise &amp; low rise buildings.</p>
      <p>We can prepare and refinish most commercial surfaces including ceilings, walls, floors, concrete floors, factory-painted metal, corrugated steel panels, steel roofs, siding, paneling and cladding. As professional commercial painters, we are capable of working in most commercial situations, including high-rise exteriors and difficult access interiors</p>
    </section>

    <section class="service">
      <h2>COLOR CONSULTING</h2>
      <p>Color creates mood and trends to you. Color gives life to your home. The best color gives unique environment to your home. We help you to enjoy the best mood by giving proper color consultation. Our creative color consultants have an excellent eye for colors and suggest you the best with the sound technical knowledge of dye, paints and fabrics.</p>
    </section>

    <section class="service">
      <h2>FENCE PAINTING</h2>
    </section>
  </main>
</body>
</html>
```